Slogan as represent the company name: cravolent

we look for a slogan which represent our company name, cravolent.
Cravolent specializes in microscopy based imaging solutions. sites: [login to view URL] and [login to view URL]
the slogan sentence should be composed of the company name letters (C.R.A.V.O.L.E.N.T) like PELUXO: All day i dream about sex/sleep!
alternatively one can make sentences to use the initials for the company banner, like below:
B: beautiful images are our goal
I: image is life
O:
I: Illumination is light as a gift of love.
M: Micro and nano precision
A: Advertisements with beautiful images & beautiful words.
G: Great performance per price products
E: Ergonomical designed microscopes
R: Resolution one is....

```html
<!DOCTYPE html>
<html lang="en">
<head>
<meta charset="utf-8">
<title>Cravolent – Acrostic Banner</title>
<link rel="stylesheet" href="https://fonts.googleapis.com/css2?family=Ubuntu:wght@300;400&display=swap">
<style>
  :root {
    --lime: #c8d94a;
    --leaf: #6f9a2a;
    --moss: #2f4a1c;
    --ink: #121a14;
    --panel: rgba(120, 170, 40, 0.62);
    --text: #ffffff;
  }
  html, body {
    margin: 0;
    padding: 0;
    width: 1200px;
    height: 800px;
    overflow: hidden;
    background: var(--ink);
  }
  .banner {
    position: relative;
    width: 1200px;
    height: 800px;
    overflow: hidden;
    font-family: "Ubuntu", sans-serif;
    color: var(--text);
  }
  .banner__photo {
    position: absolute;
    inset: 0;
    background:
      radial-gradient(ellipse 30% 45% at 55% 30%, rgba(20, 30, 28, 0.95), transparent 70%),
      radial-gradient(ellipse 18% 40% at 78% 55%, rgba(15, 22, 24, 0.95), transparent 75%),
      radial-gradient(ellipse 35% 30% at 75% 10%, rgba(240, 245, 170, 0.8), transparent 70%),
      radial-gradient(ellipse 40% 40% at 95% 50%, rgba(230, 235, 150, 0.75), transparent 70%),
      linear-gradient(100deg, var(--lime) 0%, var(--leaf) 35%, var(--moss) 70%, #3c4a2a 100%);
  }
  .banner__panel {
    position: absolute;
    left: 40px;
    top: 0;
    width: 522px;
    height: 800px;
    background: var(--panel);
  }
  .banner__title {
    position: absolute;
    left: 40px;
    top: 56px;
    width: 522px;
    margin: 0;
    text-align: center;
    font-weight: 300;
    font-size: 36px;
    letter-spacing: 0.42em;
    text-indent: 0.42em;
  }
  .acrostic {
    position: absolute;
    left: 77px;
    top: 164px;
    margin: 0;
    padding: 0;
    list-style: none;
    font-weight: 400;
    font-size: 41px;
    line-height: 55.6px;
  }
  .acrostic__line {
    display: flex;
    white-space: nowrap;
  }
  .acrostic__letter {
    width: 52px;
  }
  .acrostic__phrase::before {
    content: "- ";
  }
</style>
</head>
<body>
  <main class="banner">
    <div class="banner__photo" role="img" aria-label="Close-up photograph of microscope objective lenses against a blurred green and yellow laboratory background"></div>
    <div class="banner__panel"></div>
    <h1 class="banner__title">CRAVOLENT</h1>
    <ul class="acrostic">
      <li class="acrostic__line"><span class="acrostic__letter">C</span><span class="acrostic__phrase">Crafting</span></li>
      <li class="acrostic__line"><span class="acrostic__letter">R</span><span class="acrostic__phrase">Remarkable and</span></li>
      <li class="acrostic__line"><span class="acrostic__letter">A</span><span class="acrostic__phrase">Advanced</span></li>
      <li class="acrostic__line"><span class="acrostic__letter">V</span><span class="acrostic__phrase">Visuals in</span></li>
      <li class="acrostic__line"><span class="acrostic__letter">O</span><span class="acrostic__phrase">Optics-based</span></li>
      <li class="acrostic__line"><span class="acrostic__letter">L</span><span class="acrostic__phrase">Lab Applications</span></li>
      <li class="acrostic__line"><span class="acrostic__letter">E</span><span class="acrostic__phrase">Enabling</span></li>
      <li class="acrostic__line"><span class="acrostic__letter">N</span><span class="acrostic__phrase">New Efficiency on</span></li>
      <li class="acrostic__line"><span class="acrostic__letter">T</span><span class="acrostic__phrase">Test Results</span></li>
    </ul>
  </main>
</body>
</html>
```